Infographic that describes our service

We want to clearly explain what we offer. VOM (our company) is unique. Our members watch videos that include a real person who struggles with mental health and a clinician who analyzes their condition. The clinician breaks down the issues for our subscribers and the clinicians provides advice and coping skills that our members can apply to their own situation. The infographic must not be long/complex. It must be simple, must be a square, and must be understood in 5 second by the reader.

To better understand VOM... here's what we're not:
- online therapy
- a mental health documentary video website
- group therapy

What VOM is...
- our subscribers watch other people share their experience
- our clinicians analyze other people (not the subscriber) and breakdown those experiences so that our subscribers can learn what to do if they suffer from the same issue
- our subscribers get advice and coping skills from clinicians

Target Market(s)

People who suffer from mental health issues

Industry/Entity Type

Mental health

Requirements
Must have
• See www.seevom.tv and use our creative look and feel. Must watch our intro video on the home page to understand our service.
Nice to have
• Here is some additional language you are free to use whatever parts work best for your design... Welcome to VOM. Where real people share their struggles with you and experts analyze those struggles to give you advice and coping skills. From anxiety to depression and many more conditions, we’ve got covered. Simply browse the topics and watch. It’s a new way to heal.
Should not have
• Please don't include the website URL on the infographic - this graphic will be used on our home page, not as a standalone infographic. Please don't include a visual of a patient and therapist together on the screen at the same time. VOM works by having a person record themself, then a therapist reviews that recording and analyzes it for our subscribers. Thanks!

```html
<!DOCTYPE html>
<html lang="en">
<head>
<meta charset="utf-8">
<title>What VOM Is? – Describes Our Service</title>
<link rel="stylesheet" href="https://fonts.googleapis.com/css2?family=Montserrat:wght@600;700;800&family=Oswald:wght@700&display=swap">
<style>
  :root {
    --navy: #0c3d66;
    --navy-deep: #062c4f;
    --blue: #0062a3;
    --orange: #f47a30;
    --orange-hot: #ff6a10;
    --orange-deep: #e84c0a;
    --white: #ffffff;
    --mist: #f3f4f5;
    --rule: #e6e8ea;
  }
  * { margin: 0; padding: 0; box-sizing: border-box; }
  html, body {
    width: 1200px; height: 1200px; overflow: hidden;
    background: var(--white);
  }
  .infographic {
    position: relative; width: 1200px; height: 1200px; overflow: hidden;
    background: var(--white);
    font-family: "Montserrat", Arial, sans-serif;
  }
  .shapes { position: absolute; inset: 0; }
  .header-band {
    position: absolute; left: 247px; top: 41px; width: 953px; height: 113px;
    background: var(--navy);
  }
  .title {
    position: absolute; left: 334px; top: 40px;
    font-weight: 800; font-size: 100px; line-height: 115px;
    color: var(--white); letter-spacing: -1px; white-space: nowrap;
  }
  .subtitle {
    position: absolute; left: 332px; top: 164px;
    font-weight: 700; font-size: 57px; line-height: 66px;
    color: var(--orange); white-space: nowrap;
  }
  .brand-badge {
    position: absolute; left: 56px; top: 22px; width: 230px; height: 230px;
    border-radius: 50%; background: var(--orange);
    border: 6px solid var(--white);
    display: flex; align-items: center; justify-content: center;
  }
  .brand-name {
    font-weight: 800; font-size: 78px; color: var(--white); letter-spacing: -2px;
  }
  .point {
    position: absolute; left: 601px;
    font-weight: 700; font-size: 39px; color: var(--navy);
    white-space: nowrap;
  }
  .point-one { top: 298px; line-height: 46px; }
  .point-two { top: 538px; line-height: 50px; }
  .point-three { top: 997px; line-height: 51px; }
  .number-badge {
    position: absolute; width: 94px; height: 94px; border-radius: 50%;
    border: 4px solid var(--white);
    box-shadow: 0 6px 8px rgba(0,0,0,0.18);
    display: flex; align-items: center; justify-content: center;
    font-weight: 800; font-size: 34px; color: var(--white);
  }
  .badge-orange { background: var(--orange); }
  .badge-navy { background: var(--navy); }
  .icon-slot { position: absolute; border-radius: 14px; background: rgba(255,255,255,0.14); }
</style>
</head>
<body>
<main class="infographic">
  <svg class="shapes" width="1200" height="1200" viewBox="0 0 1200 1200" aria-hidden="true">
    <defs>
      <linearGradient id="blue-fill" x1="0" y1="0" x2="1" y2="0">
        <stop offset="0" stop-color="var(--navy-deep)"/>
        <stop offset="1" stop-color="var(--blue)"/>
      </linearGradient>
      <linearGradient id="orange-fill" x1="0" y1="0" x2="1" y2="1">
        <stop offset="0" stop-color="var(--orange-hot)"/>
        <stop offset="1" stop-color="var(--orange-deep)"/>
      </linearGradient>
    </defs>
    <circle class="backdrop-disc" cx="894" cy="909" r="384" fill="var(--mist)"/>
    <line class="divider" x1="468" y1="486" x2="1186" y2="486" stroke="var(--rule)" stroke-width="3"/>
    <line class="divider" x1="468" y1="941" x2="1186" y2="941" stroke="var(--rule)" stroke-width="3"/>
    <rect class="footer-band" x="208" y="1179" width="1020" height="60" rx="30" fill="var(--orange)"/>
    <g class="service-wheel" stroke="var(--white)" stroke-width="3" stroke-linejoin="round">
      <path d="M0,252 A475,475 0 0 1 411.4,489.5 L184.5,620.5 A213,213 0 0 0 0,514 Z" fill="url(#blue-fill)"/>
      <path d="M411.4,489.5 A475,475 0 0 1 411.4,964.5 L184.5,833.5 A213,213 0 0 0 184.5,620.5 Z" fill="url(#orange-fill)"/>
      <path d="M411.4,964.5 A475,475 0 0 1 0,1202 L0,940 A213,213 0 0 0 184.5,833.5 Z" fill="url(#blue-fill)"/>
    </g>
    <g class="connectors" fill="none" stroke="var(--navy)" stroke-width="4" stroke-linecap="round" stroke-dasharray="0 10">
      <line x1="335" y1="372" x2="582" y2="372"/>
      <line x1="493" y1="722" x2="577" y2="722"/>
      <line x1="335" y1="1074" x2="582" y2="1074"/>
    </g>
    <g class="connector-dots" fill="var(--white)" style="filter: drop-shadow(0 2px 3px rgba(0,0,0,0.25))">
      <circle cx="315" cy="372" r="16"/>
      <circle cx="473" cy="722" r="16"/>
      <circle cx="315" cy="1074" r="16"/>
    </g>
    <g class="wheel-label" font-family="Oswald, Impact, sans-serif" font-weight="700">
      <text x="27" y="699" font-size="46" fill="var(--navy)" textLength="107" lengthAdjust="spacingAndGlyphs">WHAT</text>
      <text x="27" y="759" font-size="64" fill="var(--orange)" textLength="107" lengthAdjust="spacingAndGlyphs">VOM</text>
      <text x="27" y="813" font-size="55" fill="var(--navy)" textLength="100" lengthAdjust="spacingAndGlyphs">IS??</text>
    </g>
  </svg>

  <div class="header-band"></div>
  <div class="brand-badge"><span class="brand-name">VOM</span></div>
  <h1 class="title">WHAT VOM IS?</h1>
  <h2 class="subtitle">DESCRIBES OUR SERVICE</h2>

  <div class="icon-slot" style="left:116px;top:343px;width:135px;height:136px" role="img" aria-label="Line icon of connected people and shapes"></div>
  <div class="icon-slot" style="left:294px;top:658px;width:143px;height:144px" role="img" aria-label="Line icon of a lightbulb with chart and magnifier"></div>
  <div class="icon-slot" style="left:128px;top:983px;width:125px;height:125px" role="img" aria-label="Line icon of chat bubbles, gear and person"></div>

  <div class="number-badge badge-orange" style="left:62px;top:492px">01</div>
  <div class="number-badge badge-navy" style="left:172px;top:683px">02</div>
  <div class="number-badge badge-orange" style="left:62px;top:872px">03</div>

  <p class="point point-one">Our subscribers<br>watch other people<br>share their experience</p>
  <p class="point point-two">Our clinicians analyze<br>other people (not the sub-<br>scriber) and breakdown<br>those experiences so that<br>our subscribers can learn<br>what to do if they suffer<br>from the same issue</p>
  <p class="point point-three">Our subscribers get<br>advice and coping skills<br>from clinicians</p>
</main>
</body>
</html>
```